Quillmark Letterpress Printing needs a "poster" for Vending Machine to sell mini-letterp...

I am a letterpress printer and have just purchased a small vending machine to take to craft markets/local boutiques and sell Mini-Letterpress Prints for $1 (four quarters).  Here is a link to what the machine looks like:  https://www.treatvendco.example/Heron-Decal-and-Stamp-Vending-Unit-Q4817.aspx
I need you all to design fun artwork for the front of the machine... dimensions are:  18" height, 15" width.  My company website is Quillmarkletterpress.example if you want to see my branding.  The mini-prints will constantly be changing, and each will be signed (by me).  I would like a strong "letterpress" look.... old school Brindle Yard Press type vibe.  I want it to look fun, colorful, and capture many impulse purchases.

Target Market(s)
impulse purchasers at artisan craft markets and small high end boutique stores
Requirements
Must have
- would prefer the colors to coordinate and/or mostly match my brand

Nice to have
- I would like to have a manicule on the design.... maybe: 4 quarters [manicule] 1 surprise print

Should not have
- comic sans

```html
<!DOCTYPE html>
<html lang="en">
<head>
<meta charset="utf-8">
<title>The Happy Inkwell – Vending Poster</title>
<link rel="stylesheet" href="https://fonts.googleapis.com/css2?family=Oswald:wght@600&family=Fredoka:wght@600&family=Rokkitt:wght@700&display=swap">
<style>
  :root {
    --paper: #f4efe7;
    --frame: #a3322f;
    --magenta: #e6007e;
    --purple: #8e2b8e;
    --crimson: #c41e4a;
    --cyan: #00aeef;
    --red: #ee2e24;
    --coral: #ef4136;
    --orange: #f26522;
    --gold: #f7941d;
    --yellow: #fff200;
    --green: #00a651;
    --blue: #2e9fd8;
  }
  html, body { margin: 0; padding: 0; overflow: hidden; background: var(--paper); }
  .poster { display: block; width: 1200px; height: 1071px; }
  .wordmark { font-family: "Oswald", sans-serif; font-weight: 600; }
  .title { font-family: "Oswald", sans-serif; font-weight: 600; }
  .round { font-family: "Fredoka", sans-serif; font-weight: 600; }
  .slab { font-family: "Rokkitt", serif; font-weight: 700; }
</style>
</head>
<body>
<svg class="poster" viewBox="0 0 1200 1071" xmlns="http://www.w3.org/2000/svg">
  <!-- paper and frame -->
  <rect class="paper" width="1200" height="1071" fill="var(--paper)"/>
  <rect class="frame" x="10" y="12" width="1180" height="1046" fill="none" stroke="var(--frame)" stroke-width="3"/>

  <!-- brand name at the head -->
  <text class="wordmark brand-head" x="593" y="175" text-anchor="middle" font-size="72" letter-spacing="4" fill="var(--crimson)">QUILLMARK</text>

  <!-- brand name in the corner -->
  <text class="wordmark brand-corner" x="1103" y="138" text-anchor="middle" font-size="24" fill="var(--purple)">QUILLMARK</text>

  <!-- machine title -->
  <text class="title machine-name" x="593" y="302" text-anchor="middle" font-size="86" letter-spacing="2" fill="var(--magenta)">THE HAPPY INKWELL</text>

  <line class="rule" x1="349" y1="354" x2="837" y2="354" stroke="var(--magenta)" stroke-width="3"/>

  <!-- headline -->
  <text class="round" x="354" y="439" font-size="66" letter-spacing="6" fill="var(--cyan)" textLength="481" lengthAdjust="spacingAndGlyphs">PRESS &amp; GET</text>

  <text class="round" x="95" y="547" font-size="88" fill="none" stroke="var(--magenta)" stroke-width="1.5" stroke-dasharray="2 3" textLength="1002" lengthAdjust="spacingAndGlyphs">A MINI-LETTERPRESS</text>
  <text class="round" x="92" y="544" font-size="88" fill="var(--magenta)" textLength="1002" lengthAdjust="spacingAndGlyphs">A MINI-LETTERPRESS</text>

  <g class="print-line" fill="var(--coral)">
    <polygon points="428,593 432,604 444,604 434,611 438,623 428,615 418,623 422,611 412,604 424,604"/>
    <circle cx="455" cy="608" r="2.5"/>
    <text class="round" x="469" y="634" font-size="74" letter-spacing="4" textLength="251" lengthAdjust="spacingAndGlyphs">PRINT</text>
    <circle cx="734" cy="608" r="2.5"/>
    <polygon points="749,593 753,604 765,604 755,611 759,623 749,615 739,623 743,611 733,604 745,604"/>
  </g>

  <line class="rule" x1="349" y1="671" x2="837" y2="671" stroke="var(--red)" stroke-width="3"/>

  <!-- price line -->
  <g class="slab" font-size="44">
    <text x="191" y="744" fill="var(--yellow)" textLength="263" lengthAdjust="spacingAndGlyphs">4 QUARTERS</text>
    <text x="189" y="742" fill="var(--red)" textLength="263" lengthAdjust="spacingAndGlyphs">4 QUARTERS</text>
    <text x="592" y="744" fill="var(--yellow)" textLength="425" lengthAdjust="spacingAndGlyphs">ONE SUPRISE PRINT!</text>
    <text x="590" y="742" fill="var(--magenta)" textLength="425" lengthAdjust="spacingAndGlyphs">ONE SUPRISE PRINT!</text>
  </g>
  <rect class="manicule" role="img" aria-label="Pointing hand manicule" x="475" y="711" width="87" height="34" rx="10" fill="var(--coral)"/>

  <!-- column dividers -->
  <line x1="494" y1="776" x2="494" y2="971" stroke="var(--frame)" stroke-width="2"/>
  <line x1="796" y1="773" x2="796" y2="975" stroke="var(--frame)" stroke-width="2"/>

  <!-- column: unique & signed -->
  <g class="slab col-unique">
    <text x="68" y="828" font-size="54" fill="var(--cyan)" textLength="324" lengthAdjust="spacingAndGlyphs">EACH PRINT</text>
    <text x="407" y="828" font-size="34" fill="var(--gold)" textLength="32" lengthAdjust="spacingAndGlyphs">IS</text>
    <text x="76" y="904" font-size="62" fill="var(--magenta)" textLength="225" lengthAdjust="spacingAndGlyphs">UNIQUE</text>
    <text x="352" y="904" font-size="60" fill="var(--magenta)">&amp;</text>
    <text x="349" y="901" font-size="60" fill="var(--coral)">&amp;</text>
    <text x="72" y="963" font-size="42" fill="var(--yellow)" textLength="391" lengthAdjust="spacingAndGlyphs">PERSONALLY SIGNED!</text>
    <text x="70" y="961" font-size="42" fill="var(--green)" textLength="391" lengthAdjust="spacingAndGlyphs">PERSONALLY SIGNED!</text>
  </g>

  <!-- column: hot off the press -->
  <g class="slab col-hot">
    <text x="543" y="832" font-size="58" fill="var(--yellow)" textLength="211" lengthAdjust="spacingAndGlyphs">HOT OFF</text>
    <text x="540" y="829" font-size="58" fill="var(--red)" textLength="211" lengthAdjust="spacingAndGlyphs">HOT OFF</text>
    <text x="603" y="886" font-size="38" fill="var(--gold)" textLength="67" lengthAdjust="spacingAndGlyphs">THE</text>
    <text x="557" y="947" font-size="58" fill="var(--coral)" textLength="185" lengthAdjust="spacingAndGlyphs">PRESS!</text>
  </g>

  <!-- column: perfectly imperfect -->
  <g class="slab col-imperfect">
    <text x="841" y="828" font-size="52" fill="var(--orange)" textLength="268" lengthAdjust="spacingAndGlyphs">PERFECTLY</text>
    <text x="838" y="896" font-size="58" fill="var(--yellow)" textLength="288" lengthAdjust="spacingAndGlyphs">IMPERFECT</text>
    <text x="835" y="893" font-size="58" fill="var(--green)" opacity="0.85" textLength="288" lengthAdjust="spacingAndGlyphs">IMPERFECT</text>
    <text x="832" y="891" font-size="58" fill="var(--cyan)" opacity="0.8" textLength="288" lengthAdjust="spacingAndGlyphs">IMPERFECT</text>
    <text x="849" y="948" font-size="32" fill="var(--blue)" opacity="0.6" textLength="72" lengthAdjust="spacingAndGlyphs">MINI</text>
    <text x="848" y="947" font-size="32" fill="var(--frame)" textLength="72" lengthAdjust="spacingAndGlyphs">MINI</text>
    <text x="943" y="949" font-size="48" fill="var(--blue)" opacity="0.6" textLength="160" lengthAdjust="spacingAndGlyphs">PRINTS!</text>
    <text x="940" y="947" font-size="48" fill="var(--coral)" opacity="0.9" textLength="160" lengthAdjust="spacingAndGlyphs">PRINTS!</text>
  </g>

  <!-- down arrows -->
  <g class="arrows">
    <polygon points="238,978 254,978 254,998 266,998 246,1022 226,998 238,998" fill="var(--cyan)"/>
    <polygon points="636,978 652,978 652,998 664,998 644,1022 624,998 636,998" fill="var(--magenta)"/>
    <polygon points="990,980 1006,980 1006,1000 1018,1000 998,1024 978,1000 990,1000" fill="var(--magenta)" opacity="0.3"/>
    <polygon points="987,978 1003,978 1003,998 1015,998 995,1022 975,998 987,998" fill="var(--yellow)"/>
  </g>
</svg>
</body>
</html>
```